Wordpress Web Design & Coding for velnoragroup.ca

We need a website for a new investment company that is visually grabbing and vibrant. We would like to see a web page that displays trust, growth and confidence. Needs to be responsive and mobile friendly for all browsers and coded for both Android & IOS.

Open to the number of pages and menu items. I selected 4 but if you feel the layout would work better with less I am open to this. Need to sell the people (management team/related businesses) and then show where the invested money will be going (upcoming projects).

Company Info:

Velnora is an investment company put together by a group of seasoned business professionals who have come together to combine decades of success in the real estate development, management, financing and medical services. The company will be a full service company offering turn key solutions for medical professionals.

Vel-Nora will focus on providing a full range of services via a group of distinct companies to deliver newly emerging needs of the medical community. The end goal will be to create complete solutions for individuals in the medical community. Our group has experience and success with the conceptualization, construction and financing of medical and dental clinic spaces. Vel-Nora Group will be established to accommodate all areas of the development and creation of clinics for medical professionals from building construction to equipment financing and administrations.

You can mention these companies and take photos from their websites. You can also use stock photos.

Our construction partner:
https://382bld.com/projects/

Our equipment leasing partner:
https://www.pordiva.com/

Our Management Team and medical partners

Gil Parkes
https://www.mysoundpoise.ca/

Milos Vendraker
https://www.qrtdentalservices.com/about-us

PROPOSED PROJECTS (see attachment for details)
Hollowmere Business Park
Cresfield Business Park
Mt. Corwin Ridge Professional

Investors

Investment

Sans Serif

Must have
• Wordpress – must be both desktop and mobile friendly with fast page load speed
Ability to edit after ourselves in Wordpress
Attractive home page with logo etc.
Logo colours are: for the blue the pantone color is #0355a3
and for the green is #8cc63f

Sections, about us, what we do/services we provide, contact us

```html
<!DOCTYPE html>
<html lang="en">
<head>
<meta charset="utf-8">
<title>Vel-Nora Group</title>
<link href="https://fonts.googleapis.com/css2?family=Montserrat:wght@400;500;600;700&display=swap" rel="stylesheet">
<style>
:root{
  --blue:#0355a3;
  --blue-deep:#0a4fa8;
  --green:#8cc63f;
  --ink:#1b1b1b;
  --muted:#6b6b6b;
  --rule:#ececec;
  --white:#ffffff;
}
*{margin:0;padding:0;box-sizing:border-box}
html,body{width:1200px;height:2878px;overflow:hidden}
body{position:relative;background:var(--white);font-family:'Montserrat',sans-serif;color:var(--ink)}
.abs{position:absolute}

/* hero */
.hero{left:0;top:0;width:1200px;height:791px;background:linear-gradient(100deg,#2c3136 0%,#474c50 40%,#3c434a 62%,#1e4a78 82%,#2a5c92 100%)}
.hero-shade{left:0;top:0;width:1200px;height:791px;background:rgba(20,24,28,.45)}
.nav{left:216px;top:26px;width:768px;height:50px;background:var(--white);display:flex;align-items:center;padding:0 20px 0 22px}
.brand{display:flex;align-items:center;gap:8px;font-weight:700;font-size:20px;color:var(--blue);letter-spacing:.2px;width:142px}
.brand-mark{width:16px;height:16px;background:var(--green)}
.menu{display:flex;gap:23px;font-size:11px;font-weight:500;margin-left:18px}
.menu a{color:var(--ink);text-decoration:none}
.menu a.active{color:var(--blue)}
.lang{margin-left:auto;font-size:10px;font-weight:600}
.lang span{color:#bbb;font-weight:400}
.hero-title{left:360px;top:236px;width:480px;text-align:center;color:var(--white);font-weight:700;font-size:38px;line-height:45px;letter-spacing:-.3px}
.cta{left:537px;top:419px;width:124px;height:38px;background:var(--green);color:var(--white);font-size:12px;font-weight:700;display:flex;align-items:center;justify-content:center}
.contact-row{left:235px;top:591px;width:730px;display:flex;align-items:center;color:var(--white);font-size:12px}
.contact-row b{font-weight:600}
.contact-row .phone{margin-left:30px}
.contact-row .phone b{color:var(--green)}
.follow{margin-left:auto;display:flex;align-items:center;gap:14px}
.follow i{display:block;width:9px;height:9px;border-radius:50%;background:var(--white)}
.follow i.g{background:var(--green)}

/* why choose */
.why{left:207px;top:631px;width:786px;height:475px;background:var(--blue-deep)}
.kicker{font-size:10px;font-weight:700;letter-spacing:.2px;text-align:center}
.why .kicker{left:0;top:82px;width:786px;color:var(--white)}
.why-lead{left:10px;top:155px;width:381px;text-align:right;color:var(--white);font-weight:700;font-size:21px;line-height:30px;letter-spacing:-.4px}
.feature{left:446px;width:290px;color:#cfe0f3}
.feature h3{color:var(--green);font-size:15px;font-weight:700;margin-bottom:9px;letter-spacing:-.2px}
.feature p{font-size:9px;line-height:15px}

/* grid */
.gridline{top:1106px;width:1px;height:1430px;background:var(--rule)}
.projects-kicker{left:0;top:1182px;width:1200px}
.photo{background:linear-gradient(135deg,#c9d2db,#8d9aa6 55%,#5f7ea0)}
.project-title{color:var(--green);font-weight:700;font-size:15px;line-height:15px;letter-spacing:-.2px}
.project-body{display:flex;flex-direction:column}
.project-text{font-size:9px;line-height:15px;color:var(--muted)}
.learn{font-size:9px;color:var(--green);margin-top:15px}
.vbar{width:2px;background:var(--green)}
.hbar{height:2px;background:var(--green)}
.blueprint{background:linear-gradient(180deg,#1a48aa 0%,#2652b8 50%,#1d4aa6 100%);border-top:22px solid #0f4aa0;border-bottom:22px solid #0f4aa0}
.corridor{background:linear-gradient(180deg,#8a9098 0%,#cfd4d8 45%,#e6e2da 75%,#c5c0b8 100%)}
.project-title.dark{color:var(--ink);font-size:15px}
.pricing{left:654px;top:2244px;font-size:10px;font-weight:700;text-decoration:underline;color:var(--ink)}
.security-kicker{left:0;top:2454px;width:1200px}

/* security band */
.band{left:0;top:2536px;width:1200px;height:342px;background:linear-gradient(180deg,#2a5cb0,#1d4fa3 60%,#2458ae)}
.band-note{left:360px;top:2592px;width:480px;text-align:center;color:#dfe9f7;font-size:9px;line-height:15px}
.band-quote{left:330px;top:2754px;width:540px;text-align:center;color:var(--white);font-weight:700;font-size:23px;line-height:37px;letter-spacing:-.3px}
</style>
</head>
<body>

<div class="abs hero" role="img" aria-label="Photo of a medical clinic reception desk with shelves of files and blue window blinds"></div>
<div class="abs hero-shade"></div>

<nav class="abs nav">
  <div class="brand"><span class="brand-mark"></span>VEL-NORA</div>
  <div class="menu">
    <a class="active" href="#">Home</a><a href="#">About Us</a><a href="#">What we do</a><a href="#">Solutions</a><a href="#">Contact us</a>
  </div>
  <div class="lang">ENG <span>/ FRA</span></div>
</nav>

<h1 class="abs hero-title">To assist the medical community in catering to those services</h1>
<div class="abs cta">ENQUIRE NOW!</div>

<div class="abs contact-row">
  <span>Email: <b>hello@vel-nora.com</b></span>
  <span class="phone">Phone: <b>(+012) 555-0142-77</b></span>
  <span class="follow">Follow us: <i class="g"></i><i></i><i></i><i></i><i></i></span>
</div>

<section class="abs why">
  <div class="abs kicker">WHY CHOOSE VEL-NORA</div>
  <p class="abs why-lead">We are a group of seasoned<br>business professionals who<br>have come together to<br>combine decades of<br>success in the real estate<br>development.</p>
  <div class="abs feature" style="top:156px"><h3>Professional Liability</h3><p>Donec lacinia mi rutrum sagittis consequat. Donec sagittis,<br>tellus sodales sollicitudin commodo</p></div>
  <div class="abs feature" style="top:244px"><h3>Dedicated To Our Clients</h3><p>Quisque mollis metus magna, ut<br>accumsan elit hendrerit ac. Lorem ipsum dolor sit amet,</p></div>
  <div class="abs feature" style="top:333px"><h3>Outstanding Services</h3><p>lacinia mi rutrum sagittis consequat. Donec sagittis, tellus<br>sodales sollicitudin commodo, risus urna interdum massa</p></div>
</section>

<div class="abs gridline" style="left:235px"></div>
<div class="abs gridline" style="left:479px"></div>
<div class="abs gridline" style="left:723px"></div>
<div class="abs gridline" style="left:965px"></div>

<div class="abs kicker projects-kicker">PROPOSED PROJECTS</div>

<!-- project 1 -->
<div class="abs photo" style="left:360px;top:1259px;width:363px;height:234px" role="img" aria-label="Photo of two medical staff reviewing a tablet in a glass atrium"></div>
<div class="abs project-title" style="left:779px;top:1259px;width:150px">Hollowmere<br>Business Park</div>
<div class="abs project-body" style="left:779px;top:1309px;width:150px">
  <p class="project-text">The Hollowmere Business Park in Cresfield, Westmark Province on Harlow island, is presently under contract with partners that are controlled by individuals who form part of the Vel-Nora management group. The purchase of the land will be closing early summer 2020.</p>
  <a class="learn">Learn More</a>
</div>
<div class="abs vbar" style="left:963px;top:1259px;height:80px"></div>

<!-- project 2 -->
<div class="abs hbar" style="left:235px;top:1582px;width:80px"></div>
<svg class="abs" style="left:237px;top:1623px" width="28" height="28" viewBox="0 0 28 28"><circle cx="14" cy="14" r="8" fill="none" stroke="#e0e0e0"/><path d="M14 0v28M0 14h28" stroke="#e0e0e0"/></svg>
<div class="abs project-title" style="left:360px;top:1583px;width:150px">Cresfield<br>Business Park</div>
<div class="abs project-body" style="left:360px;top:1633px;width:138px">
  <p class="project-text">The city of Cresfield is a core municipality in the Western Communities. it is currently experiencing regional increases in population driven by residential, commercial and industrial development. Cresfield projected an increase in its population of 123% by 2026. The 2016 census indicated that Cresfield ranked number i in growth among</p>
  <a class="learn">Learn More</a>
</div>
<div class="abs blueprint" style="left:546px;top:1583px;width:419px;height:286px" role="img" aria-label="Blueprint site plan of the business park"></div>

<!-- project 3 -->
<div class="abs corridor" style="left:235px;top:1960px;width:244px;height:386px" role="img" aria-label="Photo of a bright glass walkway corridor"></div>
<div class="abs vbar" style="left:589px;top:1960px;height:80px"></div>
<div class="abs project-title dark" style="left:654px;top:1960px;width:320px">Mt. Corwin Ridge Professional</div>
<div class="abs project-body" style="left:654px;top:1998px;width:312px">
  <p class="project-text">Mt. Corwin Professional building will feature a repurposed building adjacent to Mt. Corwin Ridge in Mt. Corwin, WP. This location served as a car dealership, but will be renovated from its current structure to a two storey building to house professional and medical services. The high profile location fronting Mt. Corwin Ridge sees more than 45,000 vehicles per day making it the ideal high profile location for Vel-Nora.</p>
  <a class="learn" style="margin-top:28px">Learn More</a>
</div>
<svg class="abs" style="left:577px;top:2243px" width="28" height="28" viewBox="0 0 28 28"><circle cx="14" cy="14" r="8" fill="none" stroke="#e0e0e0"/><path d="M14 0v28M0 14h28" stroke="#e0e0e0"/></svg>
<div class="abs pricing">PRICING / PLANS / PACKAGES</div>

<div class="abs kicker security-kicker">SECURITY</div>

<section class="abs band" role="img" aria-label="Blue-toned photo of a commercial building with tenant signage"></section>
<p class="abs band-note">Vel-Nora Group's leasing division will implement a number of security measures which ensures investors<br>are secure and returns are maximized over the life of the investments.</p>
<p class="abs band-quote">As we embark on this newest chapter, our combined knowledge will build on the discussions of the privatization in medical</p>

</body>
</html>
```